Laboratory marketing Flyer

I want to create a flyer that's reflective of all the services our laboratory offers. please review our services at www.qorvendiagnostics.com as well as about us for our amenities. focus more on areas of testing other than Toxicology, Covid-19 and Neutralizing anti-body titer. More so on UTI, Gastrointestinal, Wound, Genetics and respiratory. attached is a very old/outdated brochure, I want this in one page, vertical, front and back format.

Target Market(s)

medical facilities

Industry/Entity Type

medical

Font styles to use
Sans Serif

Colors
0054AA
0677BA
7BADD7
CADEEF
E8F1F8

Requirements
Must have
• Answer the phone, quick sample collection, fast turnaround time, large test menu, and Tally-Ward-Link integration

```html
<!DOCTYPE html>
<html lang="en">
<head>
<meta charset="utf-8">
<title>Qorven Diagnostics Flyer</title>
<link rel="stylesheet" href="https://fonts.googleapis.com/css2?family=Montserrat:wght@400;500;600;700;800;900&display=swap">
<style>
:root{
  --brand:#2b7bc6;
  --brand-deep:#0054aa;
  --brand-mid:#0677ba;
  --brand-soft:#7badd7;
  --brand-pale:#cadeef;
  --brand-mist:#e8f1f8;
  --ink:#3a3f47;
  --white:#ffffff;
  --stage:#f1f2f3;
}
*{box-sizing:border-box;margin:0;padding:0}
html,body{width:1200px;height:985px;overflow:hidden}
body{background:var(--stage);font-family:'Montserrat',sans-serif;position:relative;color:var(--ink)}
.sheet{position:absolute;top:149px;width:500px;height:706px;overflow:hidden;background:var(--white);box-shadow:0 6px 18px rgba(0,0,0,.12)}
.sheet--front{left:71px}
.sheet--back{left:629px}
.abs{position:absolute}
.layer{position:absolute;left:0;top:0}

/* front */
.front-haze{left:0;top:0;width:500px;height:330px;background:linear-gradient(90deg,#f4f8fc 0%,#e2ecf5 60%,#d6e4f0 100%)}
.brand-mark{left:49px;top:28px;width:142px;text-align:center}
.brand-mark__dot{width:34px;height:34px;border:2px solid var(--brand);border-radius:50%;margin:0 auto 6px}
.brand-mark__name{font-weight:700;color:var(--brand);font-size:15px;letter-spacing:.5px;line-height:1.1}
.hero-kicker{left:32px;top:146px;font-size:15px;font-weight:500;color:var(--ink)}
.hero-title{left:32px;top:164px;font-size:31px;font-weight:900;color:var(--brand);line-height:36px;letter-spacing:.5px}
.hero-sub{left:32px;top:242px;font-size:12.5px;font-weight:800;color:var(--ink);line-height:16px}
.why-title{left:37px;top:342px;font-size:14px;font-weight:700;color:var(--white);line-height:17px}
.why-title span{font-weight:400;color:var(--brand-pale)}
.why-sub{left:37px;top:383px;font-size:8px;color:var(--brand-pale)}
.why-rule{left:37px;top:398px;width:58px;height:1.5px;background:var(--brand-pale)}
.reason{left:38px;width:205px}
.reason__dot{position:absolute;left:0;top:0;width:24px;height:24px;border-radius:50%;background:var(--white)}
.reason__label{position:absolute;left:28px;top:-15px;font-size:7.5px;color:var(--brand-pale)}
.reason__text{position:absolute;left:28px;top:-3px;width:200px;font-size:6.6px;line-height:8.5px;color:var(--white)}
.facts-title{left:289px;top:402px;font-size:13.5px;font-weight:700;color:var(--white)}
.facts-sub{left:289px;top:428px;font-size:7.5px;line-height:10px;color:var(--brand-pale)}
.facts-rule{left:289px;top:451px;width:64px;height:1.5px;background:var(--brand-pale)}
.facts-list{left:289px;top:462px;width:200px;list-style:none}
.facts-list li{position:relative;padding-left:8px;font-size:5.6px;line-height:7px;color:var(--white);margin-bottom:5.5px}
.facts-list li::before{content:"";position:absolute;left:0;top:3px;width:4px;height:1px;background:var(--white)}
.amen-tab{left:155px;top:615px;width:193px;height:22px;background:var(--white);border-radius:7px 7px 0 0;text-align:center;font-size:11.5px;font-weight:700;color:var(--brand);line-height:24px}
.amen-list{list-style:none;width:210px}
.amen-list li{display:flex;align-items:center;gap:5px;font-size:8.6px;color:var(--ink);height:15.2px}
.tick{width:9px;height:9px;flex:none}

/* back */
.back-wash{left:0;top:0;width:500px;height:706px;background:linear-gradient(180deg,#ffffff 0%,#f1f6fb 28%,#c6dcf0 48%,#6fa6da 62%,var(--brand) 78%,var(--brand) 100%)}
.back-kicker{left:0;top:38px;width:500px;text-align:center;font-size:17px;font-weight:500;color:var(--ink)}
.back-title{left:0;top:62px;width:500px;text-align:center;font-size:31px;font-weight:900;color:var(--brand);letter-spacing:.4px}
.back-sub{left:0;top:103px;width:500px;text-align:center;font-size:13px;font-weight:800;color:var(--ink);line-height:20px}
.ghost-mark{left:0;top:255px;width:500px;text-align:center}
.ghost-mark__dot{width:100px;height:100px;border:3px solid rgba(123,173,215,.35);border-radius:50%;margin:0 auto 26px}
.ghost-mark__name{font-size:54px;font-weight:700;color:rgba(123,173,215,.35);letter-spacing:1px}
.mission-frame{left:25px;top:391px;width:448px;height:150px;border:2px solid rgba(0,84,170,.45);border-bottom:none;border-radius:10px 10px 0 0}
.mission{left:40px;width:420px;text-align:center;font-size:9.6px;line-height:11.5px}
.mission--lead{top:411px;color:var(--white)}
.mission--detail{top:467px;color:var(--brand-pale)}
.mission-rule{left:163px;top:529px;width:166px;height:1.5px;background:var(--white)}
.perk-row{left:0;width:500px;display:flex;justify-content:center;gap:12px}
.perk{display:flex;align-items:center;gap:4px;font-size:10.3px;font-weight:700;color:var(--white)}
.contact-rule{left:0;top:614px;width:500px;height:1.5px;background:var(--white)}
.web-pill{left:175px;top:603px;width:150px;height:23px;background:var(--white);border-radius:6px;text-align:center;font-size:9.8px;font-weight:700;color:var(--brand);line-height:23px}
.contact-line{left:0;width:500px;display:flex;justify-content:center;align-items:center;gap:18px;font-size:13px;font-weight:600;color:var(--white)}
.contact-item{display:flex;align-items:center;gap:6px}
.contact-item svg{width:14px;height:14px;flex:none}
</style>
</head>
<body>

<!-- FRONT -->
<section class="sheet sheet--front">
  <div class="abs front-haze"></div>

  <svg class="layer" width="500" height="706" viewBox="0 0 500 706">
    <polygon points="311,0 500,0 500,389 349,382 242,126" fill="#b9cfe2" role="img" aria-label="Photo of a scientist in safety glasses and blue gloves using a microscope in a lab"/>
    <polyline points="316,-2 247,126 352,378 500,386" fill="none" stroke="var(--brand)" stroke-width="4" stroke-linejoin="round"/>
    <path d="M0,321 L252,321 C300,321 312,355 336,390 C350,410 360,419 380,419 L500,419 L500,625 L0,625 Z" fill="var(--brand)"/>
  </svg>

  <div class="abs brand-mark">
    <div class="brand-mark__dot"></div>
    <div class="brand-mark__name">QORVEN<br>DIAGNOSTICS</div>
  </div>

  <div class="abs hero-kicker">AT QORVEN DIAGNOSTICS,</div>
  <div class="abs hero-title">WE STRIVE<br>TO PROVIDE</div>
  <div class="abs hero-sub">OUR PATIENTS AND PARTNERS<br>WITH THE VERY BEST.</div>

  <div class="abs why-title"><span>Why Choose</span> Qorven Diagnostics<br>as Your Partner?</div>
  <div class="abs why-sub">Precise results through the most innovative technology.</div>
  <div class="abs why-rule"></div>

  <div class="abs reason" style="top:419px">
    <div class="reason__dot"></div>
    <p class="reason__text" style="top:-3px">All of our drug safety monitoring testing will utilize the LC/MS/MS, otherwise known as the "Superior Standard" for analytical quantitation.</p>
  </div>
  <div class="abs reason" style="top:460px">
    <div class="reason__dot"></div>
    <p class="reason__text" style="top:-2px">State-of-the-art method along with precise results means you can trust Qorven Diagnostics to help formulate safety decisions for your patients.</p>
  </div>
  <div class="abs reason" style="top:511px">
    <div class="reason__dot"></div>
    <span class="reason__label" style="top:-24px">Prompt Results</span>
    <p class="reason__text" style="top:-13px">We provide our partners with industry leading 48 hr turnaround time for quantitative results. We accomplish this through the optimization of our laboratory testing procedure and by employing the most qualified and experienced laboratory staff.</p>
  </div>
  <div class="abs reason" style="top:574px">
    <div class="reason__dot"></div>
    <span class="reason__label" style="top:-20px">Comprehensive Customized Panels</span>
    <p class="reason__text" style="top:-8px">We deliver a widespread customizable offering of urine drug testing panels.</p>
  </div>

  <div class="abs facts-title">Facts</div>
  <div class="abs facts-sub">In the U.S., these factors<br>are intensified and supported by:</div>
  <div class="abs facts-rule"></div>
  <ul class="abs facts-list">
    <li>Over 4 billion prescription medications are prescribed yearly</li>
    <li>50% of patients do not take their medication as prescribed and directed</li>
    <li>55,403 drug overdoses in 2016</li>
    <li>About 20,101 of prescription drug overdoses are caused by pain killers</li>
    <li>46% of prescription drug users also take over the counter medications</li>
    <li>At least 1 in 25 Americans is on a prescription drug regimen which poses a major risk for a Drug to Drug interaction (DDI)</li>
    <li>About 32% of prescriptions are never filled</li>
    <li>In the U.S., non-adherence leads to 125K deaths annually</li>
  </ul>

  <div class="abs amen-tab">Qorven Diagnostics Amenities</div>
  <ul class="abs amen-list" style="left:32px;top:643px">
    <li><svg class="tick" viewBox="0 0 10 10"><circle cx="5" cy="5" r="5" fill="var(--brand)"/><path d="M2.8,5.2 L4.4,6.7 L7.3,3.6" fill="none" stroke="#fff" stroke-width="1.3"/></svg>Tailored collection and pick-up services</li>
    <li><svg class="tick" viewBox="0 0 10 10"><circle cx="5" cy="5" r="5" fill="var(--brand)"/><path d="M2.8,5.2 L4.4,6.7 L7.3,3.6" fill="none" stroke="#fff" stroke-width="1.3"/></svg>A widespread drug safety testing menu</li>
    <li><svg class="tick" viewBox="0 0 10 10"><circle cx="5" cy="5" r="5" fill="var(--brand)"/><path d="M2.8,5.2 L4.4,6.7 L7.3,3.6" fill="none" stroke="#fff" stroke-width="1.3"/></svg>Customizable drug testing possibilities</li>
  </ul>
  <ul class="abs amen-list" style="left:237px;top:643px;width:250px">
    <li><svg class="tick" viewBox="0 0 10 10"><circle cx="5" cy="5" r="5" fill="var(--brand)"/><path d="M2.8,5.2 L4.4,6.7 L7.3,3.6" fill="none" stroke="#fff" stroke-width="1.3"/></svg>Remote consultation with our toxicology experts</li>
    <li><svg class="tick" viewBox="0 0 10 10"><circle cx="5" cy="5" r="5" fill="var(--brand)"/><path d="M2.8,5.2 L4.4,6.7 L7.3,3.6" fill="none" stroke="#fff" stroke-width="1.3"/></svg>Simple, easy-to-read and time sensible reports</li>
    <li><svg class="tick" viewBox="0 0 10 10"><circle cx="5" cy="5" r="5" fill="var(--brand)"/><path d="M2.8,5.2 L4.4,6.7 L7.3,3.6" fill="none" stroke="#fff" stroke-width="1.3"/></svg>Numerous reporting options</li>
  </ul>
</section>

<!-- BACK -->
<section class="sheet sheet--back">
  <div class="abs back-wash"></div>

  <div class="abs back-kicker">WE PROVIDE</div>
  <div class="abs back-title">TRUSTED RESULTS</div>
  <div class="abs back-sub">THROUGH THE MOST INNOVATIVE<br>TESTING METHODS</div>

  <div class="abs ghost-mark" aria-hidden="true">
    <div class="ghost-mark__dot"></div>
    <div class="ghost-mark__name">QORVEN</div>
  </div>

  <div class="abs mission-frame"></div>
  <p class="abs mission mission--lead">At Qorven we strive at providing our patients with the best quality care by providing physicians, hospitals, medical centers, clinics, and healthcare facilities with state-of-the-art urine drug confirmation testing for the most commonly scheduled prescription drugs and narcotics.</p>
  <p class="abs mission mission--detail">The highly complex method developed by our team will most definitely detect, and confirm the presence and concentration of scheduled prescription drugs and illicit narcotics which will aid your practice in providing a lab-guided medication management program for your patients.</p>
  <div class="abs mission-rule"></div>

  <div class="abs perk-row" style="top:544px">
    <span class="perk"><svg class="tick" viewBox="0 0 10 10"><circle cx="5" cy="5" r="4.3" fill="none" stroke="#fff" stroke-width="1.3"/><path d="M2.9,5.1 L4.4,6.6 L7.2,3.7" fill="none" stroke="#fff" stroke-width="1.3"/></svg>Answer the phone</span>
    <span class="perk"><svg class="tick" viewBox="0 0 10 10"><circle cx="5" cy="5" r="4.3" fill="none" stroke="#fff" stroke-width="1.3"/><path d="M2.9,5.1 L4.4,6.6 L7.2,3.7" fill="none" stroke="#fff" stroke-width="1.3"/></svg>quick sample collection</span>
  </div>
  <div class="abs perk-row" style="top:568px;gap:8px">
    <span class="perk"><svg class="tick" viewBox="0 0 10 10"><circle cx="5" cy="5" r="4.3" fill="none" stroke="#fff" stroke-width="1.3"/><path d="M2.9,5.1 L4.4,6.6 L7.2,3.7" fill="none" stroke="#fff" stroke-width="1.3"/></svg>fast turnaround time</span>
    <span class="perk"><svg class="tick" viewBox="0 0 10 10"><circle cx="5" cy="5" r="4.3" fill="none" stroke="#fff" stroke-width="1.3"/><path d="M2.9,5.1 L4.4,6.6 L7.2,3.7" fill="none" stroke="#fff" stroke-width="1.3"/></svg>large test menu</span>
    <span class="perk"><svg class="tick" viewBox="0 0 10 10"><circle cx="5" cy="5" r="4.3" fill="none" stroke="#fff" stroke-width="1.3"/><path d="M2.9,5.1 L4.4,6.6 L7.2,3.7" fill="none" stroke="#fff" stroke-width="1.3"/></svg>Tally-Ward-Link integration</span>
  </div>

  <div class="abs contact-rule"></div>
  <div class="abs web-pill">www.qorvendiagnostics.com</div>

  <div class="abs contact-line" style="top:640px">
    <span class="contact-item"><svg viewBox="0 0 24 24"><path d="M6.6,10.8a15.2,15.2 0 0 0 6.6,6.6l2.2-2.2a1,1 0 0 1 1-.25 11.4,11.4 0 0 0 3.6.57 1,1 0 0 1 1,1V20a1,1 0 0 1-1,1A17,17 0 0 1 3,4a1,1 0 0 1 1-1h3.5a1,1 0 0 1 1,1 11.4,11.4 0 0 0 .57,3.6 1,1 0 0 1-.25,1Z" fill="#fff"/></svg>(555)014-2290</span>
    <span class="contact-item"><svg viewBox="0 0 24 24"><rect x="2" y="5" width="20" height="14" rx="1.5" fill="#fff"/><path d="M3,6 L12,13 L21,6" fill="none" stroke="var(--brand)" stroke-width="1.6"/></svg>support@qorvendiagnostics.com</span>
  </div>
  <div class="abs contact-line" style="top:664px">
    <span class="contact-item"><svg viewBox="0 0 24 24"><path d="M12,2a7,7 0 0 0-7,7c0,5.2 7,13 7,13s7-7.8 7-13a7,7 0 0 0-7-7Zm0,9.5A2.5,2.5 0 1 1 14.5,9 2.5,2.5 0 0 1 12,11.5Z" fill="#fff"/></svg>4120 Harborline Ave, Suite 210, Fairview, OH 44126</span>
  </div>
</section>

</body>
</html>
```